Client Proposal

I need a proposal template to give to potential clients detailing our services, safety, company history, table of contents and appendixes. I need a cover page to start with images describing our services. Our company is based in Grande Prairie, Alberta. We do land survey work, engineering and environmental.

In word format please so that we can change the proposal on an as needed basis.

```html
<!DOCTYPE html>
<html lang="en">
<head>
<meta charset="utf-8">
<title>Proposal Template – Cover and Contents</title>
<link href="https://fonts.googleapis.com/css2?family=Exo+2:wght@400;500;600&family=Montserrat:wght@600&display=swap" rel="stylesheet">
<style>
  :root {
    --backdrop: #000000;
    --paper: #ffffff;
    --brand-blue: #1ea6e0;
    --band-deep: #0f87c2;
    --band-light: #46b2e4;
    --photo-light: #a99679;
    --photo-dark: #8f7c5f;
    --ink: #111418;
    --rule-grey: #9a9ea3;
    --watermark: #eeeff1;
  }
  * { box-sizing: border-box; margin: 0; padding: 0; }
  html, body { width: 1200px; height: 784px; overflow: hidden; background: var(--backdrop); }
  body { position: relative; font-family: "Exo 2", sans-serif; color: var(--ink); }

  .page { position: absolute; top: 13px; width: 581px; height: 754px; background: var(--paper); overflow: hidden; }
  .page--cover { left: 12px; }
  .page--contents { left: 607px; }

  .cover-art { position: absolute; inset: 0; }

  .cover-title { position: absolute; right: 26px; top: 510px; text-align: right; color: var(--paper); }
  .cover-title h1 { font-weight: 600; font-size: 36.5px; line-height: 1; letter-spacing: -0.3px; }
  .cover-title p { font-weight: 500; font-size: 18.7px; margin-top: 9px; }

  .brand { position: absolute; display: flex; align-items: center; color: var(--brand-blue); font-family: "Exo 2", sans-serif; font-weight: 600; text-transform: uppercase; white-space: nowrap; }
  .brand__mark { background: var(--brand-blue); }
  .brand--cover { left: 27px; top: 670px; font-size: 26px; gap: 10px; }
  .brand--cover .brand__mark { width: 30px; height: 30px; }
  .brand--header { left: 418px; top: 34px; font-size: 13px; gap: 6px; }
  .brand--header .brand__mark { width: 15px; height: 15px; }

  .header-rule { position: absolute; left: 0; top: 36px; width: 410px; height: 1px; background: var(--rule-grey); }

  .watermark { position: absolute; left: 74px; top: 660px; transform: rotate(-90deg); transform-origin: 0 0; font-family: "Montserrat", sans-serif; font-weight: 600; font-size: 72px; line-height: 1; color: var(--watermark); white-space: nowrap; letter-spacing: -4px; }

  .toc { position: absolute; left: 211px; top: 100px; width: 327px; }
  .toc h2 { font-weight: 500; font-size: 21px; color: var(--brand-blue); line-height: 1; margin-bottom: 15px; }
  .toc__group + .toc__group { margin-top: 11px; }
  .toc__group--spaced { margin-top: 20px !important; }
  .toc__row { display: flex; align-items: baseline; height: 16.5px; font-size: 9px; }
  .toc__row--chapter { font-weight: 600; }
  .toc__row--item { padding-left: 7px; padding-right: 7px; }
  .toc__group--deep .toc__row--item { padding-left: 11px; padding-right: 3px; }
  .toc__leader { flex: 1; border-bottom: 1px dotted #555; margin: 0 4px; transform: translateY(-2px); }
  .toc__page { min-width: 10px; text-align: right; font-weight: 400; }
  .toc__row--item .toc__page { margin-right: -7px; }
  .toc__group--deep .toc__row--item .toc__page { margin-right: -3px; }

  .footer-rule { position: absolute; left: 40px; top: 712px; width: 498px; height: 1.5px; background: var(--brand-blue); }
  .footer-note { position: absolute; left: 40px; top: 720px; font-size: 7px; display: flex; gap: 8px; }
</style>
</head>
<body>

<section class="page page--cover">
  <svg class="cover-art" width="581" height="754" viewBox="0 0 581 754">
    <defs>
      <linearGradient id="photoTones" x1="0" y1="0" x2="0" y2="1">
        <stop offset="0" stop-color="var(--photo-light)"/>
        <stop offset="1" stop-color="var(--photo-dark)"/>
      </linearGradient>
      <linearGradient id="bandTones" x1="0" y1="0" x2="1" y2="0">
        <stop offset="0" stop-color="var(--band-deep)"/>
        <stop offset="0.45" stop-color="#1592cd"/>
        <stop offset="1" stop-color="var(--band-light)"/>
      </linearGradient>
    </defs>
    <rect role="img" aria-label="Photograph: land surveyor in hard hat and safety vest using survey equipment on a tripod in a prairie field" x="0" y="0" width="581" height="460" fill="url(#photoTones)"/>
    <polygon points="0,421 581,450 581,692 0,587" fill="url(#bandTones)"/>
  </svg>

  <div class="cover-title">
    <h1>Project Title Here</h1>
    <p>Persentator Name here</p>
  </div>

  <div class="brand brand--cover"><span class="brand__mark"></span>Ridgeway Group</div>
</section>

<section class="page page--contents">
  <div class="header-rule"></div>
  <div class="brand brand--header"><span class="brand__mark"></span>Ridgeway Group</div>

  <div class="watermark" aria-hidden="true">Table of Contents</div>

  <nav class="toc">
    <h2>Table of Contents</h2>

    <div class="toc__group">
      <div class="toc__row toc__row--chapter"><span>Introduction content title</span><span class="toc__leader"></span><span class="toc__page">2</span></div>
      <div class="toc__row toc__row--chapter"><span>Chapter 1: Page title content&nbsp; title here</span><span class="toc__leader"></span><span class="toc__page">3</span></div>
      <div class="toc__row toc__row--item"><span>Paragraph title hereParagraph title</span><span class="toc__leader"></span><span class="toc__page">3</span></div>
      <div class="toc__row toc__row--item"><span>Paragraph title hereParagraph title</span><span class="toc__leader"></span><span class="toc__page">3</span></div>
      <div class="toc__row toc__row--item"><span>Paragraph title hereParagraph title</span><span class="toc__leader"></span><span class="toc__page">4</span></div>
      <div class="toc__row toc__row--item"><span>Paragraph title hereParagraph title</span><span class="toc__leader"></span><span class="toc__page">5</span></div>
      <div class="toc__row toc__row--item"><span>Paragraph title hereParagraph title</span><span class="toc__leader"></span><span class="toc__page">5</span></div>
      <div class="toc__row toc__row--item"><span>Paragraph title hereParagraph title</span><span class="toc__leader"></span><span class="toc__page">6</span></div>
    </div>

    <div class="toc__group">
      <div class="toc__row toc__row--chapter"><span>Chapter 2: Page title content&nbsp; title here</span><span class="toc__leader"></span><span class="toc__page">8</span></div>
      <div class="toc__row toc__row--item"><span>Paragraph title hereParagraph title</span><span class="toc__leader"></span><span class="toc__page">8</span></div>
      <div class="toc__row toc__row--item"><span>Paragraph title hereParagraph title</span><span class="toc__leader"></span><span class="toc__page">8</span></div>
      <div class="toc__row toc__row--item"><span>Paragraph title hereParagraph title</span><span class="toc__leader"></span><span class="toc__page">8</span></div>
      <div class="toc__row toc__row--item"><span>Paragraph title hereParagraph title</span><span class="toc__leader"></span><span class="toc__page">11</span></div>
      <div class="toc__row toc__row--item"><span>Paragraph title hereParagraph title</span><span class="toc__leader"></span><span class="toc__page">11</span></div>
      <div class="toc__row toc__row--item"><span>Paragraph title hereParagraph title</span><span class="toc__leader"></span><span class="toc__page">12</span></div>
    </div>

    <div class="toc__group toc__group--spaced toc__group--deep">
      <div class="toc__row toc__row--chapter"><span>Chapter 3: Page title content&nbsp; title here</span><span class="toc__leader"></span><span class="toc__page">12</span></div>
      <div class="toc__row toc__row--item"><span>Paragraph title hereParagraph title</span><span class="toc__leader"></span><span class="toc__page">12</span></div>
      <div class="toc__row toc__row--item"><span>Paragraph title hereParagraph title</span><span class="toc__leader"></span><span class="toc__page">12</span></div>
      <div class="toc__row toc__row--item"><span>Paragraph title hereParagraph title</span><span class="toc__leader"></span><span class="toc__page">13</span></div>
      <div class="toc__row toc__row--item"><span>Paragraph title hereParagraph title</span><span class="toc__leader"></span><span class="toc__page">14</span></div>
      <div class="toc__row toc__row--item"><span>Paragraph title hereParagraph title</span><span class="toc__leader"></span><span class="toc__page">14</span></div>
      <div class="toc__row toc__row--item"><span>Paragraph title hereParagraph title</span><span class="toc__leader"></span><span class="toc__page">16</span></div>
    </div>

    <div class="toc__group toc__group--spaced toc__group--deep">
      <div class="toc__row toc__row--chapter"><span>Chapter 4: Page title content&nbsp; title here</span><span class="toc__leader"></span><span class="toc__page">19</span></div>
      <div class="toc__row toc__row--item"><span>Paragraph title hereParagraph title</span><span class="toc__leader"></span><span class="toc__page">19</span></div>
      <div class="toc__row toc__row--item"><span>Paragraph title hereParagraph title</span><span class="toc__leader"></span><span class="toc__page">19</span></div>
      <div class="toc__row toc__row--item"><span>Paragraph title hereParagraph title</span><span class="toc__leader"></span><span class="toc__page">20</span></div>
      <div class="toc__row toc__row--item"><span>Paragraph title hereParagraph title</span><span class="toc__leader"></span><span class="toc__page">20</span></div>
      <div class="toc__row toc__row--item"><span>Paragraph title hereParagraph title</span><span class="toc__leader"></span><span class="toc__page">22</span></div>
      <div class="toc__row toc__row--item"><span>Paragraph title hereParagraph title</span><span class="toc__leader"></span><span class="toc__page">23</span></div>
    </div>
  </nav>

  <div class="footer-rule"></div>
  <div class="footer-note"><span>1</span><span>Copyright text here</span></div>
</section>

</body>
</html>
```